Velvet corsaro

I want a business card design. the company is an infrastructure development company.

Target Market(s)

Government
real estate investors
real estate clients

Industry/Entity Type

Business

```html
<!DOCTYPE html>
<html lang="en">
<head>
<meta charset="utf-8">
<title>Velvet Corsaro — Business Card</title>
<link rel="stylesheet" href="https://fonts.googleapis.com/css2?family=Jost:ital,wght@0,400;0,500;1,400&display=swap">
<style>
  :root {
    --backdrop: #2a2a2b;
    --card: #f1f1f0;
    --ink: #1c1c1c;
    --label: #6f6f6f;
    --brand-red: #e3342f;
    --brand-blue: #2aa7df;
  }
  * { margin: 0; padding: 0; box-sizing: border-box; }
  html, body {
    width: 1200px; height: 800px; overflow: hidden;
    background: var(--backdrop);
    font-family: "Jost", "Futura", sans-serif;
    color: var(--ink);
  }
  .card {
    position: absolute;
    left: 150px; top: 140px;
    width: 900px; height: 520px;
    background: var(--card);
    box-shadow: 0 10px 30px rgba(0,0,0,0.45);
  }
  .brand {
    position: absolute;
    left: 250px; top: 70px;
    display: flex; align-items: center; gap: 16px;
  }
  .brand-square {
    width: 38px; height: 38px;
    background: var(--brand-blue);
  }
  .brand-name {
    font-weight: 400;
    font-size: 44px;
    letter-spacing: 1px;
    text-transform: uppercase;
    color: var(--brand-red);
    line-height: 1;
  }
  .holder {
    position: absolute;
    left: 70px; top: 225px;
  }
  .holder-name {
    font-size: 38px;
    font-weight: 400;
    letter-spacing: 1.5px;
  }
  .holder-role {
    font-size: 20px;
    font-style: italic;
    margin: 12px 0 0 120px;
    letter-spacing: 1px;
  }
  .contact {
    position: absolute;
    display: grid;
    grid-template-columns: auto auto;
    column-gap: 14px;
    row-gap: 8px;
    align-items: baseline;
  }
  .contact dt {
    font-size: 15px;
    font-style: italic;
    color: var(--label);
    text-align: right;
  }
  .contact dd {
    font-size: 21px;
    letter-spacing: 1px;
  }
  .contact-personal { left: 70px; top: 375px; }
  .contact-office { left: 500px; top: 180px; }
  .contact-office dd.address { line-height: 1.3; margin-bottom: 18px; }
</style>
</head>
<body>
  <article class="card">
    <div class="brand">
      <span class="brand-square"></span>
      <span class="brand-name">Velvet Corsaro</span>
    </div>

    <div class="holder">
      <h1 class="holder-name">Tunde Adeyemi</h1>
      <p class="holder-role">MD.</p>
    </div>

    <dl class="contact contact-personal">
      <dt>phone 1</dt><dd>+234 8015550142</dd>
      <dt>phone 2</dt><dd>+234 7035550187</dd>
      <dt>email</dt><dd>tunde@velvetcorsaro.com</dd>
    </dl>

    <dl class="contact contact-office">
      <dt>address</dt>
      <dd class="address">12 Marigold Street<br>Off Harbour Link Road<br>Ikeja Lagos, Nigeria</dd>
      <dt>phone 1</dt><dd>+234 15550236</dd>
      <dt>phone 2</dt><dd>+234 7055550319</dd>
      <dt>email</dt><dd>info@velvetcorsaro.com</dd>
      <dt>web</dt><dd>www.velvetcorsaro.com</dd>
    </dl>
  </article>
</body>
</html>
```